Modern Business Card Design Needed for Young Realtor

Information that is going on the card:Marcus Penhall
Broker/Owner
555.013.2967
Marcus@MPenhallHomes.example
www.MPenhallHomes.example

Would also like to include my Instagram Handle somewhere. Probably on the back: the_queencity_realtorMy previous business card is attached, I like that one but would like an updated version and maybe a few design changes

Marcus Penhall
Broker/Owner
555.013.2967
Marcus@MPenhallHomes.example
www.MPenhallHomes.example

• Would also like to include my Instagram Handle somewhere. Probably on the back: the_harborline_agent
• Brantley Osgood or the BO (logo from the previous card.)

```html
<!DOCTYPE html>
<html lang="en">
<head>
<meta charset="utf-8">
<title>MPenhallHomes Business Card</title>
<link href="https://fonts.googleapis.com/css2?family=Cinzel:wght@500&family=Montserrat:wght@400;500;700&display=swap" rel="stylesheet">
<style>
  :root{
    --stage:#cfd0d2;
    --card:#262626;
    --red:#9b1f2e;
    --white:#f4f4f4;
    --photo-a:#6f8a55;
    --photo-b:#4c4f55;
  }
  *{margin:0;padding:0;box-sizing:border-box}
  html,body{width:1200px;height:1021px;overflow:hidden}
  body{background:var(--stage);font-family:"Montserrat",Arial,sans-serif;position:relative}
  .card{position:absolute;left:250px;width:700px;height:400px;background:var(--card);
        box-shadow:0 10px 26px rgba(0,0,0,.28);overflow:hidden}
  .card--back{top:70px}
  .card--front{top:551px}

  .brand{display:flex;align-items:center;gap:12px;font-family:"Cinzel",Georgia,serif;
         font-weight:500;color:var(--white);letter-spacing:3px}
  .brand__mark{width:14px;height:14px;background:var(--red);flex:none}

  .card--back .brand{position:absolute;left:0;right:0;top:140px;justify-content:center;font-size:44px}
  .handle{position:absolute;left:0;right:0;top:262px;display:flex;flex-direction:column;
          align-items:center;gap:8px;color:var(--white);font-size:17px;letter-spacing:.3px}
  .handle__icon{width:20px;height:20px;border:2px solid var(--red);border-radius:5px}

  .front__info{position:absolute;left:0;top:0;width:400px;height:400px}
  .card--front .brand{position:absolute;left:34px;top:44px;font-size:29px}
  .agent{position:absolute;left:34px;top:122px}
  .agent__name{color:var(--red);font-weight:700;font-size:24px}
  .agent__title{color:var(--white);font-size:16px;margin-top:2px}
  .contact{position:absolute;left:34px;top:200px;list-style:none;color:var(--white);font-size:16px}
  .contact li{display:flex;align-items:center;gap:9px;margin-bottom:7px}
  .contact svg{width:15px;height:15px;flex:none}
  .band{position:absolute;left:0;top:300px;width:400px;height:48px;background:var(--red);
        display:flex;align-items:center;justify-content:space-between;padding:0 20px 0 34px}
  .band__web{color:var(--white);font-size:15px}
  .band__web b{font-weight:700}
  .badges{display:flex;gap:8px}
  .badge{width:24px;height:24px;background:var(--white)}
  .photo{position:absolute;left:400px;top:0;width:300px;height:400px;
         background:linear-gradient(180deg,var(--photo-a) 0%,#9c9a8c 45%,var(--photo-b) 100%)}
</style>
</head>
<body>
  <section class="card card--back">
    <div class="brand"><span class="brand__mark"></span>MPenhallHomes</div>
    <div class="handle"><span class="handle__icon"></span>the_harborline_agent</div>
  </section>

  <section class="card card--front">
    <div class="front__info">
      <div class="brand"><span class="brand__mark"></span>MPenhallHomes</div>
      <div class="agent">
        <div class="agent__name">Marcus Penhall</div>
        <div class="agent__title">Broker/Owner</div>
      </div>
      <ul class="contact">
        <li><svg viewBox="0 0 24 24"><path fill="#9b1f2e" d="M6.6 10.8a15 15 0 0 0 6.6 6.6l2.2-2.2a1 1 0 0 1 1-.25 11.4 11.4 0 0 0 3.6.57 1 1 0 0 1 1 1V20a1 1 0 0 1-1 1A17 17 0 0 1 3 4a1 1 0 0 1 1-1h3.5a1 1 0 0 1 1 1c0 1.25.2 2.45.57 3.57a1 1 0 0 1-.25 1z"/></svg>555.013.2967</li>
        <li><svg viewBox="0 0 24 24"><rect x="2.5" y="5" width="19" height="14" fill="none" stroke="#9b1f2e" stroke-width="2"/><path d="M3 6l9 7 9-7" fill="none" stroke="#9b1f2e" stroke-width="2"/></svg>Marcus@MPenhallHomes.example</li>
      </ul>
      <div class="band">
        <span class="band__web">www.<b>MPenhallHomes</b>.example</span>
        <div class="badges"><span class="badge"></span><span class="badge"></span></div>
      </div>
    </div>
    <div class="photo" role="img" aria-label="Portrait photo of the agent in a grey blazer, outdoors with greenery behind"></div>
  </section>
</body>
</html>
```